Window Graphics for New Dental Office

This is a bank of windows along a busy street that a new dental office wants to cover in graphics. The file ideas for window designs is the look the client is going for. The template with bleed lines .pdf is a a 10 percent scaled version of the graphics for the graphic layout. The dental window placement diagram is a picture showing the actual windows that will be covered in light green and the other .pdf is the clients logo.

This dentist wants a high end botique look with an competent and inviting feel.

You may incorporate ideas like:
- Emergency and Same Day Appointments Available
- The lead dentist works with every patient
- latest technology for crowns and veneers in-house
- free teeth whitening kit with every expert consultation
- every patient is our best patient
- Financing available
- PPO insurance and Payment Plans Accepted

```html
<!DOCTYPE html>
<html lang="en">
<head>
<meta charset="utf-8">
<title>Brightpeak Dental – Window Graphics</title>
<link rel="stylesheet" href="https://fonts.googleapis.com/css2?family=Jost:wght@500;600;700&display=swap">
<style>
  :root {
    --sky: #4ddff8;
    --mint: #c6fbf7;
    --ice: #c4f7f6;
    --steel-blue: #23769e;
    --slate: #434f55;
    --fog: #d0d6d8;
    --brand-blue: #2a6ff0;
    --ink: #4a5358;
    --white: #ffffff;
    --guide: #8fd96b;
    --rule: #b9bfc2;
  }
  * { box-sizing: border-box; margin: 0; padding: 0; }
  html, body { width: 1200px; height: 1200px; overflow: hidden; background: var(--white); }
  body { font-family: "Jost", sans-serif; position: relative; }
  .abs { position: absolute; }

  .top-band { left: 0; top: 0; width: 1200px; height: 147px; background: var(--sky); }

  .shadow-label { left: 8px; top: 259px; font-size: 11px; color: var(--slate); text-decoration: underline; }
  .shadow-line { left: 62px; top: 276px; width: 1130px; height: 1px; background: var(--rule); }

  .panel-guide { border: 1px dashed var(--guide); }

  .block { position: absolute; }
  .steel { background: var(--steel-blue); }
  .slate { background: var(--slate); }
  .sky { background: var(--sky); }
  .ice { background: var(--ice); }
  .fog { background: var(--fog); }
  .white { background: var(--white); }

  .social-tag { display: flex; align-items: center; gap: 5px; color: var(--white); font-size: 8px; font-weight: 600; }
  .social-dot { width: 9px; height: 9px; border-radius: 50%; background: var(--white); }

  .brand-name { font-weight: 600; color: var(--brand-blue); line-height: 1.02; letter-spacing: 0.5px; text-transform: uppercase; text-align: left; }
  .brand-mark { display: flex; align-items: center; gap: 10px; }
  .brand-square { background: var(--brand-blue); flex: none; }

  .vertical { transform: rotate(-90deg); transform-origin: center; }

  .window-divider { width: 2px; background: var(--slate); opacity: 0.8; }

  .feature-list-small { list-style: none; color: var(--white); font-size: 7px; font-weight: 700; text-transform: uppercase; letter-spacing: 0.2px; }
  .feature-list-small li { height: 17.3px; }

  .mint-band { left: 0; top: 611px; width: 1200px; height: 288px; background: var(--mint); }
  .feature-list { list-style: none; color: var(--ink); font-size: 18px; font-weight: 600; letter-spacing: 0.3px; }
  .feature-list li { height: 28.8px; }

  .storefront { left: 0; top: 899px; width: 599px; height: 301px;
    background: linear-gradient(180deg, #e9eef2 0%, #d9d4cc 45%, #9fb58a 70%, #7d8a80 100%); }
</style>
</head>
<body>
  <div class="abs top-band"></div>

  <div class="abs shadow-label">Shadow Line</div>
  <div class="abs shadow-line"></div>

  <!-- Left window panel -->
  <section class="abs panel-guide" style="left:69px; top:176px; width:145px; height:386px;">
    <div class="block steel" style="left:0; top:0; width:143px; height:100px;">
      <div class="social-tag abs" style="left:16px; top:78px;"><span class="social-dot"></span>Brightpeak Dental</div>
    </div>
    <div class="block ice" style="left:0; top:100px; width:143px; height:208px;">
      <div class="abs vertical" style="left:-37px; top:86px; width:220px; height:36px; display:flex; align-items:center; justify-content:center;">
        <div class="brand-mark"><span class="brand-square" style="width:14px;height:14px;"></span><div class="brand-name" style="font-size:16px;">Brightpeak<br>Dental</div></div>
      </div>
    </div>
    <div class="block slate" style="left:0; top:317px; width:143px; height:67px;"></div>
  </section>

  <!-- Main window panel -->
  <section class="abs panel-guide" style="left:230px; top:176px; width:779px; height:386px;">
    <div class="block steel" style="left:0; top:0; width:157px; height:100px;"></div>
    <div class="block slate" style="left:157px; top:0; width:243px; height:100px;"></div>
    <div class="block sky" style="left:400px; top:0; width:168px; height:100px;"></div>
    <div class="block ice" style="left:568px; top:0; width:209px; height:100px; display:flex; align-items:center; justify-content:center;">
      <div class="brand-mark"><span class="brand-square" style="width:18px;height:18px;"></span><div class="brand-name" style="font-size:18px;">Brightpeak<br>Dental</div></div>
    </div>

    <div class="block white" style="left:0; top:100px; width:400px; height:208px; display:flex; align-items:center; justify-content:center;">
      <div class="brand-mark"><span class="brand-square" style="width:34px;height:34px;"></span><div class="brand-name" style="font-size:38px;">Brightpeak<br>Dental</div></div>
    </div>
    <div class="block window-divider" style="left:156px; top:100px; height:208px;"></div>
    <div class="block window-divider" style="left:310px; top:100px; height:208px;"></div>
    <div class="block fog" style="left:400px; top:100px; width:168px; height:208px;"></div>
    <div class="block slate" style="left:568px; top:100px; width:209px; height:208px;">
      <ul class="feature-list-small abs" style="left:19px; top:50px;">
        <li>Emergency and same day appointments available</li>
        <li>The lead dentist works with every patient</li>
        <li>Latest technology for crowns and veneers in-house</li>
        <li>Free teeth whitening kit with every expert consultation</li>
        <li>Every patient is our best patient</li>
        <li>Financing available</li>
        <li>PPO insurance and payment plans accepted</li>
      </ul>
    </div>

    <div class="block sky" style="left:0; top:317px; width:400px; height:67px;"></div>
    <div class="block steel" style="left:400px; top:317px; width:377px; height:67px;">
      <div class="social-tag abs" style="left:13px; top:29px;"><span class="social-dot"></span>Brightpeak Dental</div>
    </div>
  </section>

  <!-- Right window panel -->
  <section class="abs panel-guide" style="left:1025px; top:176px; width:159px; height:386px;">
    <div class="block steel" style="left:0; top:0; width:157px; height:100px;"></div>
    <div class="block fog" style="left:0; top:100px; width:157px; height:284px;">
      <div class="abs vertical" style="left:-62px; top:120px; width:280px; height:46px; display:flex; align-items:center; justify-content:center;">
        <div class="brand-mark"><span class="brand-square" style="width:20px;height:20px;"></span><div class="brand-name" style="font-size:22px;">Brightpeak<br>Dental</div></div>
      </div>
    </div>
  </section>

  <!-- Message band -->
  <section class="abs mint-band">
    <div class="abs brand-mark" style="left:135px; top:102px;">
      <span class="brand-square" style="width:36px;height:36px;"></span>
      <div class="brand-name" style="font-size:40px;">Brightpeak<br>Dental</div>
    </div>
    <ul class="feature-list abs" style="left:689px; top:42px;">
      <li>Emergency and Same Day Appointments Available</li>
      <li>The lead dentist works with every patient</li>
      <li>Latest technology for crowns and veneers in-house</li>
      <li>Free teeth whitening kit with every expert consultation</li>
      <li>Every patient is our best patient</li>
      <li>Financing available</li>
      <li>PPO insurance and Payment Plans Accepted</li>
    </ul>
  </section>

  <!-- Placement reference -->
  <div class="abs storefront" role="img" aria-label="Photo of the clinic storefront on the street, with the window bank to be covered highlighted in light green"></div>

  <div class="abs brand-mark" style="left:790px; top:1012px;">
    <span class="brand-square" style="width:30px;height:30px;"></span>
    <div class="brand-name" style="font-size:32px;">Brightpeak<br>Dental</div>
  </div>
</body>
</html>
```